Flyer-Design für Betreuer von Altenwohn- und Pflegeheimen
Zielgruppe
Die vaxo-pro GmbH betreut Altenwohn- und Pflegeheime im Bereich Arbeitsschutz.
Die Bereiche sind:
- Beratung & Schulung für Arbeitssicherheit, Erste Hilfe und Brandschutz
- Prüfung von Arbeitsmitteln und Medizingeräten
- Reparatur& Wartung von Elektrogeräten
- ein Partner für die 'Lösung aus einer Hand'
Die Zielgruppe sind die Betreiber (Inhaber) und Leitungen von Pflegeeinrichtungen für ältere Menschen und MEnschen mit Behidnerungen
Aufgabenstellung
Das Format soll quadratisch analog dem Logo der vaxo-pro GmbH mit einer Seitenlänge von 210mm sein (Breite DIN A4). Der Folder soll einmal gefaltet sein..
Das Logo beschreibt die Leistungen der vaxo-pro
- linkes oberes Quadrat = 'Beratung&Schulung'
- rechtes oberes Quadrat = 'Prüfung'
- linkes unteres Quadrat = 'Reparatur & Wartung'
- rechtes unteres Quadrat mit dem Haken = 'ein Partner ('...alles aus einer Hand!' <-- wobei mir persönlich diese Wortwahl nicht gefällt')
Der Folder soll auf der ersten Seite beim Leser das Gefühl wecken: 'Das MUSS ich lesen...' <-- Neugierde wecken.
Die beiden Innenseiten sollen die jeweiligen Quadrate der Leistungen beschreiben (siehe oben)
Die Rückseite enthält Angaben zu Referenzen und die Kontaktdaten.
Die Referenzen sollen 'allgemein' gehalten werden:
• kommunale Betreiber
• gemeinnützige Betreiber mit vielen Einrichtungen in ganz Bayern
• viele kleine Einrichtungen mit wenigen Betten ebenso wie
• private große Betreiber mit 1500 Pflegeplätzen und mehr
Karte mit Bullets von Bayern (siehe hochgeladene Datei) - vorerst dieses Bild, in der finalen Version soll diese Karte nicht so sehr nach Plurimo aussehen.
Weieter habe jetzt noch Texte als Word-Datei hinzugefügt...

```html
<!DOCTYPE html>
<html lang="de">
<head>
<meta charset="utf-8">
<title>vaxo-pro Folder</title>
<link href="https://fonts.googleapis.com/css2?family=Open+Sans:wght@400;600&display=swap" rel="stylesheet">
<style>
:root{
  --bg:#a9adb8;
  --page:#ffffff;
  --ink:#5c5c5c;
  --accent:#f2b600;
  --mark:#7a7a7a;
  --map:#dfe3e0;
}
*{box-sizing:border-box;margin:0;padding:0}
html,body{width:1200px;height:3637px;overflow:hidden}
body{background:var(--bg);font-family:"Open Sans",Arial,sans-serif;color:var(--ink);position:relative}
.page{position:absolute;width:575px;height:575px;background:var(--page);box-shadow:0 4px 14px rgba(0,0,0,.25);overflow:hidden}
.p-back{left:17px;top:1150px}
.p-cover{left:608px;top:1150px}
.p-inner-left{left:17px;top:1850px}
.p-inner-right{left:608px;top:1850px}
.block{position:absolute}
.brand{position:absolute;display:flex;align-items:center;gap:9px;font-size:30px;font-weight:400;color:var(--ink);line-height:1}
.brand-square{width:22px;height:22px;border:2px solid var(--mark)}
.text{font-size:14px;line-height:20px;color:var(--ink)}
.accent{color:var(--accent)}
.photo{position:absolute}
.photo-hands{left:0;top:245px;width:420px;height:108px;background:linear-gradient(90deg,#1d2a44 0%,#3a4560 30%,#d9a88c 55%,#e9eef4 80%,#ffffff 100%)}
.map{left:315px;top:26px;width:230px;height:200px;background:radial-gradient(circle at 50% 45%,#eef1ee 0%,var(--map) 70%,#cfd5d1 100%)}
.photo-office{left:30px;top:240px;width:230px;height:305px;background:linear-gradient(160deg,#9aa7a9 0%,#7e8a8c 40%,#b6806a 65%,#e6e6e6 100%)}
.photo-meeting{left:30px;top:315px;width:255px;height:140px;background:linear-gradient(120deg,#2b2f38 0%,#6f8a5c 45%,#a7b39a 65%,#3c3a3d 100%)}
.headline{font-size:40px;line-height:48px;font-weight:400;color:var(--ink)}
.section-title{display:flex;align-items:center;gap:9px;font-size:22px;line-height:28px;font-weight:400;color:var(--ink);margin-bottom:12px}
.section-title::before{content:"";width:16px;height:16px;background:var(--mark);display:block}
.item-title{font-size:14px;line-height:19px;color:var(--accent)}
.item-text{font-size:14px;line-height:19px;color:var(--ink);margin-bottom:6px}
.refs{list-style:none}
.refs li{font-size:14px;line-height:20px;padding-left:16px;position:relative}
.refs li::before{content:"";position:absolute;left:2px;top:8px;width:6px;height:6px;background:var(--accent)}
.arrow{position:absolute;overflow:visible}
.partner{font-size:32px;line-height:40px;display:flex;align-items:center;gap:8px;color:var(--ink)}
.partner-sub{font-size:19px;line-height:26px;color:var(--ink);margin-top:4px}
</style>
</head>
<body>

<section class="page p-back">
  <div class="brand" style="left:30px;top:26px"><span class="brand-square"></span>vaxo-pro</div>
  <div class="block text" style="left:30px;top:74px">
    vaxo-pro GmbH<br>Lindenweg 14<br>83022 Rosenheim
    <div style="margin-top:12px">Telefon: <span class="accent">+49 (8031) 40217-0</span><br>E-Mail:&nbsp;&nbsp;<span class="accent">info@vaxo-pro.de</span></div>
  </div>
  <div class="photo map" role="img" aria-label="Karte von Bayern mit Standortpunkten der betreuten Einrichtungen"></div>
  <div class="photo photo-hands" role="img" aria-label="Foto: Handschlag zweier Geschäftspartner"></div>
  <p class="block text" style="left:30px;top:366px;width:515px">Wir, die vaxo-pro GmbH, stehen für rundum-Service aus einer Hand. Mit uns an Ihrer Seite sind Sie für alle Problemfälle bei Ihren medizinischen Geräten gerüstet.</p>
  <div class="block" style="left:30px;top:436px;width:515px">
    <h2 class="section-title" style="font-size:20px;margin-bottom:6px">Referenzen</h2>
    <ul class="refs">
      <li>kommunale Betreiber</li>
      <li>gemeinnützige Betreiber mit vielen Einrichtungen in ganz Bayern</li>
      <li>viele kleine Einrichtungen mit wenigen Betten ebenso wie</li>
      <li>private große Betreiber mit 1500 Pflegeplätzen und mehr</li>
    </ul>
  </div>
</section>

<section class="page p-cover">
  <div class="brand" style="left:30px;top:26px"><span class="brand-square"></span>vaxo-pro</div>
  <h1 class="block headline" style="left:30px;top:76px">Professionell,<br>Effizient und Sicher!</h1>
  <p class="block text" style="left:30px;top:180px;width:420px">Mit vaxo-pro haben Sie einen starken, zuverlässigen Partner, der sich allen Bereichen annimmt.</p>
  <div class="photo photo-office" role="img" aria-label="Foto: jubelnde Frau am Schreibtisch im Büro"></div>
  <p class="block headline" style="left:282px;top:380px;font-size:34px;line-height:42px">Überzeugen<br>Sie sich selbst!</p>
  <svg class="arrow" style="left:420px;top:480px" width="120" height="40" viewBox="0 0 120 40"><path d="M2 36 Q55 28 112 10" fill="none" stroke="var(--accent)" stroke-width="3"/><path d="M98 6 L113 10 L104 22" fill="none" stroke="var(--accent)" stroke-width="3"/></svg>
</section>

<section class="page p-inner-left">
  <div class="block" style="left:30px;top:24px;width:515px">
    <h2 class="section-title">Beratung &amp; Schulung</h2>
    <div class="item-title">Individuelle Beratung</div>
    <p class="item-text">Alle notwendigen Prozesse werden mit Ihnen definiert.</p>
    <div class="item-title">Unterweisung</div>
    <p class="item-text">Wir führen die Unterweisung und Schulung Ihrer Mitarbeiter durch und erstellen die entsprechende Dokumentation der Schulungsmaßnahmen.</p>
    <div class="item-title">Schutzmaßnahmen</div>
    <p class="item-text">Zusammen finden wir die kosteneffizienteste &amp; rechtssichere Umsetzung Ihrer Arbeitsschutzmaßnahmen.</p>
    <div class="item-title">Gefährdenbeurteilung</div>
    <p class="item-text">Es wird die Gefährdenbeurteilung der Arbeitsplätze ihrer Mitarbeiter erstellt.</p>
    <h2 class="section-title" style="margin-top:26px">Reparatur &amp; Wartung</h2>
    <p class="item-text">Die vaxo-pro führt alle Reparaturen Ihrer defekten Geräte durch. Durch unsere sehr gut ausgestatteten und gut strukturierten Servicemobile können wir viele Reparaturen direkt vor Ort schnell und effizient durchführen. Das erhöht die Verfügbarkeit Ihrer Geräte.</p>
  </div>
  <svg class="arrow" style="left:280px;top:32px" width="110" height="26" viewBox="0 0 110 26"><path d="M2 12 Q50 5 102 16" fill="none" stroke="var(--accent)" stroke-width="3"/><path d="M91 7 L103 16 L90 23" fill="none" stroke="var(--accent)" stroke-width="3"/></svg>
  <svg class="arrow" style="left:450px;top:282px" width="80" height="60" viewBox="0 0 80 60"><path d="M72 2 Q58 42 10 54" fill="none" stroke="var(--accent)" stroke-width="3"/><path d="M18 42 L8 54 L22 60" fill="none" stroke="var(--accent)" stroke-width="3"/></svg>
  <div class="brand" style="left:30px;top:476px;font-size:28px"><span class="brand-square"></span>vaxo-pro</div>
  <p class="block text" style="left:220px;top:470px;font-size:14px;line-height:20px">Informieren Sie sich auf unserer Homepage:<br><span class="accent">www.vaxo-pro.de</span><br>Oder rufen Sie uns gerne an!<br><span class="accent">Telefon: +49 (8031) 40217-0</span></p>
</section>

<section class="page p-inner-right">
  <div class="block" style="left:30px;top:24px;width:515px">
    <h2 class="section-title">Prüfung</h2>
    <p class="item-text" style="margin-bottom:0">Arbeitsmittel, aktive Medizinprodukte und individuelle Prüffristen werden ermittelt.</p>
    <div class="item-title" style="margin-bottom:6px">Geldsparend</div>
    <p class="item-text" style="margin-bottom:0">Die Überprüfung wird periodisch überprüft und die Ergebnisse dokumentiert.</p>
    <div class="item-title" style="margin-bottom:6px">Rechtssicher</div>
    <p class="item-text" style="margin-bottom:0">Im Zuge der Überprüfung werden eventuelle Mängel &amp; dementsprechend notwendige Maßnahmen erfasst.</p>
    <div class="item-title" style="margin-bottom:6px">Effizient</div>
    <p class="item-text" style="margin-bottom:0">Nach der Prüfung wird für alle notwendigen Reparaturmaßnahmen ein Kostenrahmen erstellt.</p>
    <div class="item-title">Schafft Vertrauen</div>
  </div>
  <div class="photo photo-meeting" role="img" aria-label="Foto: zwei Geschäftsleute im Gespräch am Laptop im Freien"></div>
  <div class="block" style="left:300px;top:345px;width:250px">
    <div class="partner">Ein Partner
      <svg width="38" height="30" viewBox="0 0 52 40"><path d="M4 20 L18 34 L48 4" fill="none" stroke="var(--accent)" stroke-width="5"/></svg>
    </div>
    <p class="partner-sub">...hier kommt alles zusammen</p>
  </div>
  <div class="block" style="left:30px;top:472px;width:515px">
    <p class="item-text" style="font-size:13px;margin-bottom:8px">Wir, die vaxo-pro sind der starke Partner, den Sie als Betreiber von Wohn- oder Pflegeheimen im Gesundheitswesen brauchen.</p>
    <p class="item-text" style="font-size:13px">Denn besonders im Gesundheitswesen unterliegen Sie vielen rechtlichen Forderungen und Bestimmungen.</p>
  </div>
</section>

</body>
</html>
```